Willow Bend Senior Care

Just had our logo redesigned and want to get all supporting collateral, business cards, postcards, brochure, etc to go together, but the business cards are the current priority.
We are an agency who provides care for seniors to help them with activities of daily living and companionship in their own home. I have attached our color guidelines and our logo, as well as a copy of our current card for your reference. Our clients are seniors 65+ We would like to see something somewhat conservative but creative (we are getting rid of the desert background), double sided full color (back should have our mission statement and services as it does in the current one) Thanks a million for looking! I am looking forward to seeing what you come up with!
Target Market(s)
65+ baby boomers and 80+ Seniors
Industry/Entity Type
Conservative

```html
<!DOCTYPE html>
<html lang="en">
<head>
<meta charset="utf-8">
<title>Willow Bend Senior Care – Business Card</title>
<link href="https://fonts.googleapis.com/css2?family=Roboto+Condensed:wght@400;700&family=Montserrat:wght@700&display=swap" rel="stylesheet">
<style>
  :root {
    --navy: #1c3f6e;
    --green: #7dc242;
    --ink: #1f3a63;
    --paper: #ffffff;
    --backdrop: #e9eaec;
    --badge-navy: #2a4a7a;
    --badge-red: #b8323a;
    --badge-plum: #6e2a5c;
    --badge-blue: #2d6fb3;
  }
  * { margin: 0; padding: 0; box-sizing: border-box; }
  html, body { width: 1031px; height: 1200px; overflow: hidden; }
  body {
    background: var(--backdrop);
    font-family: "Roboto Condensed", "Arial Narrow", sans-serif;
    color: var(--ink);
    position: relative;
  }
  .card {
    position: absolute;
    left: 155px;
    width: 720px;
    height: 436px;
    background: var(--paper);
    overflow: hidden;
  }
  .card--front { top: 123px; }
  .card--back { top: 657px; }

  .top-rule { position: absolute; left: 0; right: 0; top: 0; height: 6px; background: var(--navy); }
  .bottom-rule { position: absolute; left: 0; right: 0; top: 412px; height: 4px; background: var(--navy); }
  .bottom-band { position: absolute; left: 0; right: 0; top: 420px; height: 16px; background: var(--green); }

  /* brand */
  .brand {
    position: absolute; left: 0; right: 0; top: 62px;
    display: flex; justify-content: center; align-items: center; gap: 18px;
    color: var(--navy);
    font-family: "Montserrat", Arial, sans-serif;
    font-weight: 700;
  }
  .brand__mark { width: 62px; height: 62px; border-radius: 50%; background: var(--green); }
  .brand__name { text-align: center; line-height: 1; }
  .brand__title { display: block; font-size: 56px; letter-spacing: -1px; }
  .brand__sub { display: block; font-size: 24px; letter-spacing: 7px; margin-top: 6px; }

  /* identity */
  .identity {
    position: absolute; right: 384px; top: 228px; text-align: right;
  }
  .identity__name { font-size: 27px; font-weight: 700; letter-spacing: 0.5px; color: var(--navy); line-height: 1.1; }
  .identity__role { font-size: 16px; color: var(--navy); margin-top: 1px; }
  .identity__address { font-size: 19px; color: var(--navy); margin-top: 22px; line-height: 1.25; }
  .identity__address svg { width: 15px; height: 18px; vertical-align: -2px; margin-right: 5px; }

  .divider { position: absolute; left: 338px; top: 228px; width: 3px; height: 118px; background: var(--navy); }

  .contact { position: absolute; left: 362px; top: 228px; list-style: none; }
  .contact li { font-size: 19px; color: var(--navy); height: 31px; display: flex; align-items: center; gap: 8px; }
  .contact svg { width: 16px; height: 16px; flex: none; fill: var(--green); }

  /* back */
  .mission {
    position: absolute; left: 0; right: 0; top: 0; height: 64px;
    background: var(--navy); color: #fff;
    display: flex; align-items: center; justify-content: center;
    font-size: 25px; letter-spacing: 0.5px;
  }
  .services { position: absolute; top: 90px; list-style: none; }
  .services--left { left: 70px; }
  .services--right { left: 378px; }
  .services li { font-size: 21px; height: 28px; display: flex; align-items: center; color: var(--navy); }
  .services li::before {
    content: ""; width: 7px; height: 7px; background: var(--green);
    transform: rotate(45deg); margin-right: 14px; flex: none;
  }
  .members-label {
    position: absolute; left: 0; right: 0; top: 276px; text-align: center;
    font-size: 21px; color: var(--navy);
  }
  .badge { position: absolute; }
  .badge--assoc { left: 77px; top: 272px; width: 82px; height: 112px; background: var(--badge-navy); border-radius: 4px; }
  .badge--chamber { left: 195px; top: 305px; width: 126px; height: 66px; background: var(--badge-plum); border-radius: 4px; }
  .badge--hospice { left: 360px; top: 312px; width: 160px; height: 58px; background: var(--badge-red); border-radius: 4px; }
  .badge--accredit { left: 533px; top: 270px; width: 78px; height: 124px; background: var(--badge-blue); border-radius: 6px; }
</style>
</head>
<body>

<section class="card card--front" aria-label="Business card front">
  <div class="top-rule"></div>
  <div class="brand">
    <span class="brand__name">
      <span class="brand__title">Willow Bend</span>
      <span class="brand__sub">SENIOR CARE</span>
    </span>
    <span class="brand__mark" aria-hidden="true"></span>
  </div>

  <div class="identity">
    <div class="identity__name">DANA WHITFIELD</div>
    <div class="identity__role">CEO / Executive Director</div>
    <div class="identity__address">
      <svg viewBox="0 0 15 18" aria-hidden="true"><path d="M7.5 0C3.4 0 0 3.2 0 7.2 0 12.3 7.5 18 7.5 18S15 12.3 15 7.2C15 3.2 11.6 0 7.5 0zm0 10a2.8 2.8 0 1 1 0-5.6 2.8 2.8 0 0 1 0 5.6z" fill="#7dc242"/></svg>1280 W. Alder Road<br>Tucson AZ 85704
    </div>
  </div>

  <div class="divider"></div>

  <ul class="contact">
    <li><svg viewBox="0 0 16 16" aria-hidden="true"><path d="M3.5 1 6 3.8 4.6 5.6c.9 2 2.8 3.9 4.8 4.8l1.8-1.4L14 11.5 12.3 15C6.5 14.6 1.4 9.5 1 3.7z"/></svg>520.555.0142</li>
    <li><svg viewBox="0 0 16 16" aria-hidden="true"><path d="M4 1h8v4H4zM1 6h14v7h-3v-3H4v3H1zM5 11h6v4H5z"/></svg>520.555.0187</li>
    <li><svg viewBox="0 0 16 16" aria-hidden="true"><path d="M8 1a7 7 0 1 0 0 14A7 7 0 0 0 8 1zm0 1.6c.8.9 1.4 2.2 1.6 4H6.4C6.6 4.8 7.2 3.5 8 2.6zM2.7 7.4h2.2c.1 1.5.4 2.8.9 4a5.4 5.4 0 0 1-3.1-4zm0-.8a5.4 5.4 0 0 1 3.1-4c-.5 1.2-.8 2.5-.9 4zm5.3 6.8c-.8-.9-1.4-2.3-1.6-4.2h3.2c-.2 1.9-.8 3.3-1.6 4.2zm2.2-2c.5-1.2.8-2.5.9-4h2.2a5.4 5.4 0 0 1-3.1 4zm.9-4.8c-.1-1.5-.4-2.8-.9-4a5.4 5.4 0 0 1 3.1 4z"/></svg>www.WillowBendCare.com</li>
    <li><svg viewBox="0 0 16 16" aria-hidden="true"><path d="M1 3h14v10H1z"/></svg>dana@willowbendcare.com</li>
  </ul>

  <div class="bottom-rule"></div>
  <div class="bottom-band"></div>
</section>

<section class="card card--back" aria-label="Business card back">
  <div class="mission">COMPASSION, RESPECT DEPENDABILITY...</div>

  <ul class="services services--left">
    <li>Companionship</li>
    <li>Errands and Doctor's Visits</li>
    <li>Personal Care</li>
    <li>Medication management</li>
    <li>Advocacy</li>
  </ul>
  <ul class="services services--right">
    <li>Light housekeeping</li>
    <li>Meal preparation</li>
    <li>Assisted Living placement</li>
    <li>Dementia and Alzheimer's Care</li>
    <li>Bonded and Insured</li>
  </ul>

  <div class="members-label">PROUD MEMBERS:</div>
  <div class="badge badge--assoc" role="img" aria-label="Homecare association membership badge"></div>
  <div class="badge badge--chamber" role="img" aria-label="Chamber of commerce membership badge"></div>
  <div class="badge badge--hospice" role="img" aria-label="Home care and hospice association badge"></div>
  <div class="badge badge--accredit" role="img" aria-label="Business accreditation badge"></div>

  <div class="bottom-rule"></div>
  <div class="bottom-band"></div>
</section>

</body>
</html>
```